Redesign Craft Brewing Recipe Website

Originally built with Bootstrap just to get the site going, I am seeking a complete redesign of the sites home page and recipe page. I am an experienced web developer with no graphic background, initially just looking for psd mocks.

I prefer styles that are clean and modern, and would prefer anything that is fun, engaging, and has an organic feel to it. I currently have a cartoon rabbit as a logo, but it needs some modification/tweaking, so any help in that area would be great as well.

Current site:
http://kettlefinch.hostgridapps.net/

Current launch page/logo:
http://www.kettlefinch.com/

I like the overall layout of the elements currently, but the design sucks.
Updates

The launch page is at the following URL

Reason: Still looking for a more modern design. Designs received so far are too similar to the original.

My site is content based and does not contain images or products. Your design should not consist of large images.

Reason: The website has very little images, so the designs need to be more text and content based. The header needs to be very small and should not contain an ad rotater.

Target Market(s)

Home brewers, Craft brewers, Microbreweries, Brewpubs

Requirements
Must have
• Web 2.0 Look and Feel, Fun, Hip, Focus on content
Should not have
• A large photo as a header

```html
<!DOCTYPE html>
<html lang="en">
<head>
<meta charset="utf-8">
<title>Kettlefinch – Craft Beer Recipes</title>
<link href="https://fonts.googleapis.com/css2?family=Roboto+Condensed:wght@700&family=Arimo:wght@400;700&display=swap" rel="stylesheet">
<style>
  :root{
    --top-strip:#1e4f7f;
    --sky:#2e7fc4;
    --sky-light:#3b95d6;
    --navy:#1f4d78;
    --footer:#1c4466;
    --cyan:#17b4ea;
    --cyan-dark:#0d9fd6;
    --panel:#f1f5f9;
    --card:#ffffff;
    --card-head:#efefef;
    --line:#dcdfe3;
    --ink:#555a5f;
    --ink-soft:#6b7075;
    --link:#2a8fd0;
    --green:#9ccc1c;
    --grey-tag:#707070;
    --stat:#efefef;
  }
  *{box-sizing:border-box;margin:0;padding:0}
  html,body{width:889px;height:1200px;overflow:hidden}
  body{position:relative;font-family:"Arimo",Arial,sans-serif;background:#fff;color:var(--ink)}
  .heading{font-family:"Roboto Condensed","Arial Narrow",sans-serif;font-weight:700;text-transform:uppercase}

  .hero-bg{position:absolute;left:0;top:0;width:889px;height:616px;
    background:radial-gradient(ellipse 60% 70% at 50% 55%,var(--sky-light),var(--sky) 70%,#2a73b6)}
  .top-strip{position:absolute;left:0;top:0;width:889px;height:7px;background:var(--top-strip)}
  .footer-bg{position:absolute;left:0;top:1094px;width:889px;height:106px;background:var(--footer)}

  .brand{position:absolute;left:88px;top:22px;font-size:26px;letter-spacing:2px;color:#eef4fa}
  .login{position:absolute;left:710px;top:0;width:88px;height:29px;background:var(--navy);
    clip-path:polygon(0 0,100% 0,94% 100%,6% 100%);display:flex;align-items:center;justify-content:center;gap:6px;
    color:#4fb0ea;font-size:13px;letter-spacing:1px}

  .groove{position:absolute;left:82px;width:718px;height:10px;border-radius:50%;
    background:radial-gradient(ellipse at center,rgba(20,60,110,.55),rgba(20,60,110,0) 70%)}
  .tagline{position:absolute;left:0;top:110px;width:889px;text-align:center;color:#fff;font-size:22px;line-height:27px;
    text-shadow:0 1px 2px rgba(0,0,0,.35)}

  .tab{position:absolute;top:214px;height:35px;display:flex;align-items:center;justify-content:center;font-size:13.5px;border-radius:3px 3px 0 0}
  .tab-recent{left:318px;width:61px;background:#fff;color:#2a7fc2}
  .tab-popular{left:385px;width:70px;background:var(--cyan);color:#fff}

  .panel{position:absolute;left:89px;top:249px;width:711px;height:880px;background:var(--panel);border-radius:4px;box-shadow:0 1px 3px rgba(0,0,0,.15)}

  .social{position:absolute;left:20px;top:20px;display:flex;gap:6px;font-size:7px}
  .social span{border:1px solid #c8ccd0;background:#fff;padding:1px 3px;border-radius:2px;color:#3a5a90}
  .social .count{color:#555}

  .sidebar{position:absolute;left:8px;top:44px;width:206px}
  .search{background:var(--cyan-dark);padding:5px;display:flex;gap:6px;height:34px}
  .search .field{flex:1;background:#fff;border:1px solid #c9d6e0;font-size:10.5px;color:#9a9ea2;padding:5px 7px}
  .search .go{width:27px;background:#e4e6e8;color:#a6a9ac;font-size:12px;display:flex;align-items:center;justify-content:center}
  .side-head{position:relative;height:31px;background:linear-gradient(#20c3f4,var(--cyan-dark));color:#fff;font-size:13px;letter-spacing:1px;padding:9px 10px}
  .side-head::after{content:"";position:absolute;right:20px;bottom:-5px;border:5px solid transparent;border-bottom:0;border-top-color:var(--cyan-dark)}
  .side-list{background:#fff;border:1px solid var(--line);border-top:0;list-style:none;padding:4px 0;position:relative}
  .side-list li{height:27px;display:flex;align-items:center;gap:9px;padding-left:16px;font-size:10.5px;color:#777;border-bottom:1px solid #eceef0}
  .side-list li:last-child{border-bottom:0}
  .side-list.styles li{border-bottom:0}
  .box{width:9px;height:9px;border:1px solid #a9adb1;background:linear-gradient(#fff,#e6e8ea)}
  .scroll{position:absolute;right:6px;top:10px;width:8px;height:200px;border:1px solid #c3c6c9;border-radius:4px;background:#f4f4f4}
  .scroll::after{content:"";position:absolute;left:1px;top:20px;width:4px;height:55px;background:#555;border-radius:2px}

  .card{position:absolute;left:229px;width:475px;height:200px;background:var(--card);border:1px solid var(--line);border-radius:3px}
  .card-title{height:34px;background:var(--card-head);border-bottom:1px solid var(--line);font-size:13px;color:#555;padding:10px 11px}
  .card-desc{font-size:8.5px;line-height:13px;color:#555;padding:9px 8px 0}
  .card-meta{display:flex;align-items:center;font-size:8.5px;padding:5px 8px 0;height:32px}
  .card-meta a{color:var(--link);text-decoration:none;margin-left:3px}
  .tag{color:#fff;font-size:10.5px;height:22px;display:flex;align-items:center;justify-content:center;border-radius:2px;margin-left:9px}
  .tag-method{background:var(--green);width:59px;margin-left:10px}
  .tag-style{background:var(--grey-tag);width:78px}
  .card-stats{position:absolute;left:0;top:120px;width:100%;border-top:1px solid var(--line)}
  .stat{position:absolute;top:12px;width:56px;height:56px;background:var(--stat);border-radius:3px;box-shadow:1px 2px 2px rgba(0,0,0,.18);
    text-align:center;font-size:10px;color:#666;padding-top:13px;line-height:18px}
  .stat b{display:block}

  .footer{position:absolute;left:0;top:1147px;width:889px;text-align:center;color:#e6eef6;font-size:8.5px;line-height:13.5px;letter-spacing:.3px}
</style>
</head>
<body>
  <div class="hero-bg"></div>
  <div class="top-strip"></div>
  <div class="footer-bg"></div>

  <header>
    <div class="brand heading">Kettlefinch</div>
    <a class="login heading">
      <svg width="12" height="12" viewBox="0 0 12 12"><circle cx="6" cy="3.5" r="3" fill="#4fb0ea"/><path d="M0 12c0-4 2.5-5.5 6-5.5S12 8 12 12z" fill="#4fb0ea"/></svg>
      Login
    </a>
    <div class="groove" style="top:80px"></div>
    <h1 class="tagline heading">Kettlefinch is the easiest way to create and<br>share craft beer recipes.</h1>
    <div class="groove" style="top:190px"></div>
  </header>

  <nav>
    <div class="tab tab-recent heading">Recent</div>
    <div class="tab tab-popular heading">Popular</div>
  </nav>

  <main class="panel">
    <div class="social"><span>Like</span><span class="count">3k</span><span>Share</span><span class="count">316</span></div>

    <aside class="sidebar">
      <div class="search"><div class="field">Stout</div><div class="go heading">Go</div></div>

      <div class="side-head heading">Brewing</div>
      <ul class="side-list">
        <li><span class="box"></span>Extract</li>
        <li><span class="box"></span>Partial Mash</li>
        <li><span class="box"></span>All Grain</li>
      </ul>

      <div class="side-head heading">Styles</div>
      <ul class="side-list styles">
        <li><span class="box"></span>American Amber Ale</li>
        <li><span class="box"></span>American Barleywine</li>
        <li><span class="box"></span>American Brown Ale</li>
        <li><span class="box"></span>American IPA</li>
        <li><span class="box"></span>American Pale Ale</li>
        <li><span class="box"></span>American Stout</li>
        <li><span class="box"></span>American Wheat or Rye Beer</li>
        <li><span class="box"></span>Applewine</li>
        <div class="scroll"></div>
      </ul>

      <div class="side-head heading">Match Maker</div>
      <ul class="side-list">
        <li><span class="box"></span>Boil Size</li>
      </ul>
    </aside>

    <article class="card" style="top:17px">
      <h2 class="card-title heading">Oak Bastard Sweet Mead</h2>
      <p class="card-desc">Lorem ipsum dolor sit amet, consectetur adipisicing elit, sed do eiusmod tempor incididunt ut labore et dolore magna aliqua.</p>
      <div class="card-meta">created by<a>Dana Whitlow</a><span class="tag tag-method">Extract</span><span class="tag tag-style">Sweet Mead</span></div>
      <div class="card-stats">
        <div class="stat" style="left:38px"><b>2.24%</b>abv</div>
        <div class="stat" style="left:125px"><b>24</b>ibu</div>
        <div class="stat" style="left:211px"><b>1.006</b>fg</div>
        <div class="stat" style="left:298px"><b>1.022</b>og</div>
        <div class="stat" style="left:384px"><b>4</b>srm</div>
      </div>
    </article>

    <article class="card" style="top:233px">
      <h2 class="card-title heading">Honeysucker Belgian Tripel</h2>
      <p class="card-desc">Lorem ipsum dolor sit amet, consectetur adipisicing elit, sed do eiusmod tempor incididunt ut labore et dolore magna aliqua.</p>
      <div class="card-meta">created by<a>Dana Whitlow</a><span class="tag tag-method">Extract</span><span class="tag tag-style">Sweet Mead</span></div>
      <div class="card-stats">
        <div class="stat" style="left:38px"><b>2.24%</b>abv</div>
        <div class="stat" style="left:125px"><b>24</b>ibu</div>
        <div class="stat" style="left:211px"><b>1.006</b>fg</div>
        <div class="stat" style="left:298px"><b>1.022</b>og</div>
        <div class="stat" style="left:384px"><b>4</b>srm</div>
      </div>
    </article>

    <article class="card" style="top:450px">
      <h2 class="card-title heading">Capitol Dunkelweizen</h2>
      <p class="card-desc">Lorem ipsum dolor sit amet, consectetur adipisicing elit, sed do eiusmod tempor incididunt ut labore et dolore magna aliqua.</p>
      <div class="card-meta">created by<a>Dana Whitlow</a><span class="tag tag-method">Extract</span><span class="tag tag-style">Sweet Mead</span></div>
      <div class="card-stats">
        <div class="stat" style="left:38px"><b>2.24%</b>abv</div>
        <div class="stat" style="left:125px"><b>24</b>ibu</div>
        <div class="stat" style="left:211px"><b>1.006</b>fg</div>
        <div class="stat" style="left:298px"><b>1.022</b>og</div>
        <div class="stat" style="left:384px"><b>4</b>srm</div>
      </div>
    </article>

    <article class="card" style="top:665px">
      <h2 class="card-title heading">Honeysucker Traditional Bock</h2>
      <p class="card-desc">Lorem ipsum dolor sit amet, consectetur adipisicing elit, sed do eiusmod tempor incididunt ut labore et dolore magna aliqua.</p>
      <div class="card-meta">created by<a>Dana Whitlow</a><span class="tag tag-method">Extract</span><span class="tag tag-style">Sweet Mead</span></div>
      <div class="card-stats">
        <div class="stat" style="left:38px"><b>2.24%</b>abv</div>
        <div class="stat" style="left:125px"><b>24</b>ibu</div>
        <div class="stat" style="left:211px"><b>1.006</b>fg</div>
        <div class="stat" style="left:298px"><b>1.022</b>og</div>
        <div class="stat" style="left:384px"><b>4</b>srm</div>
      </div>
    </article>
  </main>

  <footer class="footer">
    © Kettlefinch, Inc. All third party content © their respective owners.<br>
    Terms of Service | Contact
  </footer>
</body>
</html>
```